Bref créative
Stationery, etc. for a tax preparation company
looking for creative designs!
Professional
Gordon Pallister
4829 Brevard Court, Suite 100
Edina, Minnesota 55812
gordy@gordyvalmor.com
www.gptaxhelpers.com
We'd like something a little bit creative that stands out.
We'd like the back of the business card to be a lighter color so someone could write on it, if necessary.

```html
<!DOCTYPE html>
<html lang="en">
<head>
<meta charset="utf-8">
<title>GP Tax Helpers — Stationery Concepts</title>
<link rel="stylesheet" href="https://fonts.googleapis.com/css2?family=Cinzel:wght@600&family=Lato:wght@400&display=swap">
<style>
  :root {
    --backdrop: #e6ddd0;
    --paper: #ffffff;
    --purple: #4b2a55;
    --purple-deep: #33193c;
    --purple-soft: #6d4477;
    --lavender: #eee7f1;
    --lavender-deep: #ddd0e3;
    --grey: #66666b;
    --grey-deep: #45454a;
    --faint: #ececee;
    --ink: #6a6a6a;
    --label: #7a6e62;
    --shadow: 0 2px 6px rgba(60, 40, 20, .28);
  }
  * { box-sizing: border-box; margin: 0; padding: 0; }
  html, body { width: 1200px; height: 446px; overflow: hidden; }
  body {
    position: relative;
    background: var(--backdrop);
    font-family: "Lato", Arial, sans-serif;
    color: var(--ink);
  }
  .label {
    position: absolute;
    font-size: 6px;
    letter-spacing: .8px;
    text-transform: uppercase;
    color: var(--label);
    white-space: nowrap;
  }
  .sheet { position: absolute; background: var(--paper); box-shadow: var(--shadow); overflow: hidden; }
  .brand {
    display: flex; flex-direction: column; align-items: center; gap: 3px;
    font-family: "Cinzel", Georgia, serif; font-weight: 600;
    color: var(--purple); white-space: nowrap; line-height: 1;
  }
  .brand-dot { border-radius: 50%; background: var(--purple); flex: none; }
  .watermark {
    position: absolute; border-radius: 50% 50% 18% 18%;
    background: radial-gradient(ellipse at 50% 40%, var(--faint) 0%, #f3f3f4 60%, rgba(255,255,255,0) 75%);
  }

  /* business cards */
  .card { left: 19px; width: 72px; height: 44px; }
  .card-front { top: 158px; }
  .card-front .brand { position: absolute; top: 5px; left: 0; right: 0; font-size: 4.4px; }
  .card-front .brand-dot { width: 12px; height: 12px; }
  .card-front .details {
    position: absolute; left: 0; right: 0; bottom: 4px; text-align: center;
    font-size: 3px; line-height: 1.4;
  }
  .card-back {
    top: 228px; height: 50px;
    background: linear-gradient(135deg, var(--lavender), var(--lavender-deep));
  }
  .card-back .watermark { left: 18px; top: 6px; width: 36px; height: 38px;
    background: radial-gradient(ellipse at 50% 45%, #cdbcd5 0%, rgba(205,188,213,0) 72%); }

  /* letterheads */
  .letterhead { top: 19px; width: 288px; height: 394px; }
  .letterhead-one { left: 168px; }
  .letterhead-two { left: 475px; }
  .letterhead .brand { position: absolute; top: 8px; left: 50%; transform: translateX(-50%); font-size: 5.5px; }
  .letterhead .brand-dot { width: 20px; height: 20px; }
  .letterhead .watermark { left: 60px; top: 190px; width: 170px; height: 180px; }
  .letterhead-two .watermark { top: 50px; height: 170px; }
  .letterhead-one .contact {
    position: absolute; top: 10px; left: 208px;
    font-size: 3.6px; line-height: 1.7;
  }
  .contact-line::before {
    content: ""; display: inline-block; width: 3px; height: 3px;
    margin-right: 3px; background: var(--purple); vertical-align: middle;
  }
  .letterhead-two .footer {
    position: absolute; bottom: 12px; left: 0; right: 0;
    text-align: center; font-size: 3.6px;
  }

  /* envelopes */
  .envelope { left: 840px; width: 340px; }
  .envelope svg { position: absolute; inset: 0; display: block; }
  .envelope-purple { top: 7px; height: 78px; }
  .envelope-grey { top: 91px; height: 60px; }
  .envelope-logo { top: 144px; height: 100px; }
  .envelope-logo .brand { position: absolute; top: 44px; left: 50%; transform: translateX(-50%); font-size: 5px; }
  .envelope-logo .brand-dot { width: 16px; height: 16px; }
  .envelope-closed { left: 799px; top: 250px; width: 381px; height: 116px; }
  .envelope-closed .brand { position: absolute; top: 12px; left: 22px; font-size: 5.5px; }
  .envelope-closed .brand-dot { width: 20px; height: 20px; }
  .envelope-closed .return-address {
    position: absolute; top: 46px; left: 12px; width: 80px; text-align: center;
    font-size: 3.4px; line-height: 1.5;
  }
</style>
</head>
<body>
  <p class="label" style="left:19px; top:128px;">Stationery Concepts</p>

  <section class="sheet card card-front" aria-label="Business card front">
    <div class="brand"><span class="brand-dot"></span>GP Tax Helpers</div>
    <p class="details">Marla Ostrand · 2170 Linden Row, Suite 210<br>marla@gptaxhelpers.com</p>
  </section>
  <p class="label" style="left:19px; top:207px;">Business Card Front</p>

  <section class="sheet card card-back" aria-label="Business card back">
    <div class="watermark" role="img" aria-label="Faint tree decoration on a light writable back"></div>
  </section>
  <p class="label" style="left:19px; top:284px;">Business Card Back</p>

  <section class="sheet letterhead letterhead-one" aria-label="Letterhead option 1">
    <div class="brand"><span class="brand-dot"></span>GP Tax Helpers</div>
    <div class="contact">
      <div class="contact-line">2170 Linden Row, Suite 210</div>
      <div class="contact-line">Edina, Minnesota 55436</div>
      <div class="contact-line">marla@gptaxhelpers.com</div>
      <div class="contact-line">www.gptaxhelpers.net</div>
    </div>
    <div class="watermark" role="img" aria-label="Large faint tree decoration"></div>
  </section>
  <p class="label" style="left:282px; top:424px;">Letterhead Option 1</p>

  <section class="sheet letterhead letterhead-two" aria-label="Letterhead option 2">
    <div class="brand"><span class="brand-dot"></span>GP Tax Helpers</div>
    <div class="watermark" role="img" aria-label="Large faint tree decoration"></div>
    <p class="footer">2170 Linden Row, Suite 210 &nbsp;•&nbsp; Edina, Minnesota 55436 &nbsp;•&nbsp; marla@gptaxhelpers.com &nbsp;•&nbsp; www.gptaxhelpers.net</p>
  </section>
  <p class="label" style="left:589px; top:424px;">Letterhead Option 2</p>

  <section class="sheet envelope envelope-purple" aria-label="Envelope back with purple flap">
    <svg width="340" height="78" viewBox="0 0 340 78">
      <defs>
        <linearGradient id="flapPurple" x1="0" y1="0" x2="0" y2="1">
          <stop offset="0" stop-color="#6d4477"/><stop offset="1" stop-color="#3a1e44"/>
        </linearGradient>
      </defs>
      <rect width="340" height="78" fill="url(#flapPurple)"/>
      <polygon points="0,78 170,44 340,78" fill="#ffffff" opacity=".08"/>
    </svg>
  </section>

  <section class="sheet envelope envelope-grey" aria-label="Envelope back with grey flap">
    <svg width="340" height="60" viewBox="0 0 340 60">
      <rect width="340" height="60" fill="#f4f4f4"/>
      <polygon points="0,0 340,0 340,16 170,52 0,16" fill="#66666b"/>
      <polygon points="0,0 340,0 340,8 170,40 0,8" fill="#45454a"/>
    </svg>
  </section>

  <section class="sheet envelope envelope-logo" aria-label="Envelope back with purple flap and name">
    <svg width="340" height="100" viewBox="0 0 340 100">
      <rect width="340" height="100" fill="#ffffff"/>
      <polygon points="0,0 340,0 340,10 170,44 0,10" fill="#4b2a55"/>
      <polygon points="0,100 170,66 340,100" fill="#f1f1f1"/>
    </svg>
    <div class="brand"><span class="brand-dot"></span>GP Tax Helpers</div>
  </section>

  <section class="sheet envelope-closed" aria-label="Envelope option 1 front">
    <div class="brand"><span class="brand-dot"></span>GP Tax Helpers</div>
    <p class="return-address">2170 Linden Row, Suite 210<br>Edina, Minnesota 55436</p>
  </section>
  <p class="label" style="left:935px; top:388px;">Envelope Option 1</p>
</body>
</html>
```